FurryAsk.net Skin

I need a header image, backgroundand partial colour scheme for our website furryask.net.

We use a cms so have very limited ability to change the design.

We can change: link / button colour, header size and image, background image.
See these examples: http://replies.mockupvista.org/ and http://aid.zelwick.org/

Target Market(s)

Pet owners are the audience, probably slightly more females than males.

Number of Pages Required

1 page

Requirements
Nice to have
• Should be friendly and fun with an "organic" feel. Can contain images of pets but it isn"t a requirement.

```html
<!DOCTYPE html>
<html lang="en">
<head>
<meta charset="utf-8">
<title>FurryAsk.net</title>
<link rel="stylesheet" href="https://fonts.googleapis.com/css2?family=Arimo:wght@400;700&family=Open+Sans:wght@400;600;700&display=swap">
<style>
:root{
  --frame:#b98d4f;
  --white:#ffffff;
  --teal:#0e8a87;
  --orange:#f39200;
  --orange-text:#c27a00;
  --panel:#f1f1f1;
  --panel-line:#dcdcdc;
  --side:#e9e9e9;
  --ink:#111;
  --muted:#888;
  --avatar:#5cbfc0;
}
*{box-sizing:border-box;margin:0;padding:0}
html,body{width:887px;height:1200px;overflow:hidden}
body{position:relative;background:linear-gradient(#333 0,#3d3d3d 60%,#555 100%);font-family:"Open Sans",sans-serif;color:var(--ink)}
.abs{position:absolute}
.page{left:101px;top:0;width:684px;height:1200px;background:var(--frame)}
.page-inner{left:105px;top:4px;width:677px;height:1196px;background:var(--white)}
.brand{left:135px;top:34px;font-family:"Arimo",sans-serif;font-weight:700;font-size:28px;line-height:1;color:var(--orange)}
.join{left:557px;top:40px;font-family:"Arimo",sans-serif;font-weight:700;font-size:17px;color:var(--teal)}
.join small{font-size:12px}
.ask-btn{left:615px;top:32px;width:136px;height:34px;background:var(--teal);border:1px solid #3bb8b3;border-radius:3px;color:#fff;font-family:"Arimo",sans-serif;font-weight:700;font-size:12.5px;display:flex;align-items:center;justify-content:center}
.nav{left:465px;top:101px;display:flex;height:25px}
.nav a{display:flex;align-items:center;justify-content:center;font-family:"Arimo",sans-serif;font-weight:700;font-size:11px;text-decoration:none;color:#222;background:linear-gradient(#ddd,#bbb);border-radius:5px 5px 0 0}
.nav .home{width:74px;color:#fff;background:linear-gradient(#f6a21c,#e58600)}
.nav .help{width:69px;color:#fff;background:linear-gradient(#6a6a6a,#4a4a4a)}
.nav .signin{width:68px}
.nav .signup{width:75px}
.banner{left:0;top:127px;width:887px;height:245px;background:#6a6a6a}
.banner-inner{left:3px;top:130px;width:881px;height:239px;background:radial-gradient(circle at 30% 20%,#c27a10 0,#b06a05 40%,#e88a00 80%)}
.pups{left:185px;top:175px;width:232px;height:154px;border-radius:40px;background:radial-gradient(ellipse,#cdb59a 0,#9c8468 55%,rgba(176,106,5,0) 75%)}
.arrow{top:240px}
.qbox{left:440px;top:188px;width:239px;height:128px;border:2px solid rgba(255,200,120,.6);border-radius:4px;background:rgba(200,120,20,.55);padding:10px 8px;color:#fff}
.qbox h2{font-family:"Arimo",sans-serif;font-size:12.5px;font-weight:700;margin-bottom:9px}
.qbox p{font-size:8.4px;line-height:12.3px;width:218px}
.qbox .more{display:block;text-align:right;font-size:7px;font-weight:700;text-decoration:underline;margin-top:1px;padding-right:17px}
.panel{background:var(--panel);border:1px solid var(--panel-line)}
.ask{left:127px;top:399px;width:426px;height:246px}
.heading{font-family:"Arimo",sans-serif;font-weight:700;font-size:16.5px;color:var(--teal)}
.rule{height:1px;background:var(--orange)}
.avatar{width:56px;height:56px;border:1px solid #777;background:#fff;padding:3px}
.avatar span{display:block;width:100%;height:100%;background:var(--avatar)}
.field{background:#fff;border:1px solid #bbb}
.placeholder{font-size:7.5px;font-weight:600;color:#aaa;padding:7px 15px}
.ask-q{left:425px;top:599px;width:104px;height:22px;border-radius:3px;background:linear-gradient(#f7a21e,#e07f00);border:1px solid #b86500;color:#fff;font-family:"Arimo",sans-serif;font-size:12.5px;font-weight:700;display:flex;align-items:center;justify-content:center}
.latest{left:127px;top:663px;width:426px;height:54px;border-bottom:none}
.tabs{left:333px;top:682px;display:flex;gap:8px}
.tabs span{width:61px;height:21px;border-radius:3px 3px 0 0;background:linear-gradient(#d5d5d5,#b5b5b5);font-size:8px;font-weight:700;display:flex;align-items:center;justify-content:center}
.tabs .on{background:var(--orange);color:#fff}
.questions{left:127px;top:713px;width:426px;display:flex;flex-direction:column;gap:3px}
.item{position:relative;height:79px}
.item .avatar{position:absolute;left:8px;top:6px}
.item p{position:absolute;left:76px;top:5px;font-size:10.3px;line-height:12px;letter-spacing:.2px}
.item .by{position:absolute;left:76px;top:51px;font-size:8.5px;color:var(--muted)}
.item .name{position:absolute;left:152px;top:45px;width:54px;height:16px;background:#fff;border:1px solid #ccc;font-size:8.5px;color:var(--orange-text);font-weight:600;display:flex;align-items:center;justify-content:center}
.pager{left:127px;top:1126px;width:319px;height:29px;background:linear-gradient(#aaa,#eee);font-size:7.5px;font-weight:700;display:flex;align-items:center;padding-left:12px;letter-spacing:.6px;word-spacing:2px}
.search{left:578px;top:400px;width:146px;height:21px;border-radius:11px;background:#e0e0e0;border:1px solid #999;font-size:8px;color:#777;padding:4px 8px;letter-spacing:.5px}
.side{left:577px;top:445px;width:175px;height:673px;background:var(--side);border:1px solid #ddd}
.badge{left:697px;top:428px;width:62px;height:55px;background:var(--teal);border:2px solid #3bb8b3;border-radius:7px;color:#fff;text-align:center;font-family:"Arimo",sans-serif}
.badge b{display:block;font-size:20px;margin-top:7px}
.badge small{font-size:8.5px}
.side-h{font-family:"Arimo",sans-serif;font-size:12.5px;font-weight:400;color:#111}
.side-text{font-size:8.3px;line-height:12.3px;color:#222}
.member{left:586px;width:156px;height:52px;background:#fff;border:1px solid #ccc;box-shadow:0 0 0 1px #eee}
.member .ph{position:absolute;left:6px;top:6px;width:38px;height:38px;background:#c5c5c5}
.member .n{position:absolute;left:55px;top:16px;font-size:8.5px;font-weight:600;color:var(--teal);letter-spacing:.3px}
.member .a{position:absolute;left:55px;top:30px;width:84px;font-size:7px;font-weight:700;color:#666;letter-spacing:.7px;display:flex;justify-content:space-between}
.tag{left:585px;height:15px;background:#fff;border:1px solid #ccc;font-size:7px;font-weight:600;color:#aaa;letter-spacing:.8px;display:flex;justify-content:space-between;align-items:center;padding:0 6px}
.footer{left:105px;top:1174px;width:677px;height:26px;background:linear-gradient(#c97800,#f39600);font-size:7.5px;font-weight:700;display:flex;justify-content:flex-end;align-items:center;padding-right:29px;letter-spacing:.5px;word-spacing:3px}
</style>
</head>
<body>
<div class="abs page"></div>
<div class="abs page-inner"></div>

<header>
  <div class="abs brand">furryask</div>
  <div class="abs join">Join <small>or</small></div>
  <a class="abs ask-btn">ASK A QUESTION</a>
  <nav class="abs nav">
    <a class="home">Home</a><a class="help">Help</a><a class="signin">Sign In</a><a class="signup">Sign up</a>
  </nav>
</header>

<section>
  <div class="abs banner"></div>
  <div class="abs banner-inner"></div>
  <div class="abs pups" role="img" aria-label="Photo of three pug puppies sitting side by side"></div>
  <svg class="abs arrow" style="left:147px" width="34" height="25" viewBox="0 0 34 25"><path d="M14 0 L0 12.5 L14 25 L20 25 L8 12.5 L20 0Z M28 0 L14 12.5 L28 25 L34 25 L22 12.5 L34 0Z" fill="#4a4a4a" stroke="#ddd" stroke-width="1"/></svg>
  <svg class="abs arrow" style="left:698px" width="34" height="25" viewBox="0 0 34 25"><path d="M20 0 L34 12.5 L20 25 L14 25 L26 12.5 L14 0Z M6 0 L20 12.5 L6 25 L0 25 L12 12.5 L0 0Z" fill="#4a4a4a" stroke="#ddd" stroke-width="1"/></svg>
  <div class="abs qbox">
    <h2>HAVE A QUESTION?</h2>
    <p>Lorem Ipsum is simply dummy text of the printing and typesetting industry. Lorem Ipsum has been the industry's standard dummy text ever since the 1500s, when an unknown printer took a galley of type and scrambled it to make a type specimen book.</p>
    <span class="more">More</span>
  </div>
</section>

<main>
  <div class="abs panel ask"></div>
  <h2 class="abs heading" style="left:135px;top:405px">Ask a Question:</h2>
  <div class="abs rule" style="left:135px;top:425px;width:394px"></div>
  <div class="abs avatar" style="left:135px;top:446px"><span></span></div>
  <div class="abs field" style="left:205px;top:446px;width:325px;height:147px"></div>
  <div class="abs field placeholder" style="left:205px;top:599px;width:139px;height:22px">Tag this question</div>
  <a class="abs ask-q">Ask Question</a>

  <div class="abs panel latest"></div>
  <h2 class="abs heading" style="left:135px;top:682px">Latest Questions:</h2>
  <div class="abs tabs"><span class="on">Questions</span><span>Popular</span><span>Activity</span></div>
  <div class="abs rule" style="left:135px;top:702px;width:395px"></div>

  <div class="abs questions">
    <div class="item panel"><div class="avatar"><span></span></div><p>Lorem Ipsum is simply dummy text of the printing<br>and typesetting industry?</p><span class="by">Asked by Lorum</span><span class="name">Name</span></div>
    <div class="item panel"><div class="avatar"><span></span></div><p>Lorem Ipsum is simply dummy text of the printing<br>and typesetting industry?</p><span class="by">Asked by Lorum</span><span class="name">Name</span></div>
    <div class="item panel"><div class="avatar"><span></span></div><p>Lorem Ipsum is simply dummy text of the printing<br>and typesetting industry?</p><span class="by">Asked by Lorum</span><span class="name">Name</span></div>
    <div class="item panel"><div class="avatar"><span></span></div><p>Lorem Ipsum is simply dummy text of the printing<br>and typesetting industry?</p><span class="by">Asked by Lorum</span><span class="name">Name</span></div>
    <div class="item panel"><div class="avatar"><span></span></div><p>Lorem Ipsum is simply dummy text of the printing<br>and typesetting industry?</p><span class="by">Asked by Lorum</span><span class="name">Name</span></div>
  </div>

  <div class="abs pager">1 | 2 | 3 | 4 | 5 | ......... | 243 | 244 | 245 &nbsp;&nbsp;&lt;&lt;Next&gt;&gt;</div>
</main>

<aside>
  <div class="abs search">Search</div>
  <svg class="abs" style="left:729px;top:403px" width="19" height="19" viewBox="0 0 19 19"><circle cx="7.5" cy="7.5" r="6" fill="none" stroke="#bbb" stroke-width="2"/><path d="M12 12 L17.5 17.5" stroke="#bbb" stroke-width="3" stroke-linecap="round"/></svg>
  <div class="abs side"></div>
  <div class="abs badge"><b>385</b><small>Members</small></div>
  <h3 class="abs side-h" style="left:585px;top:467px">Welcome</h3>
  <p class="abs side-text" style="left:585px;top:491px;width:150px">FurryAsk.net is Q&amp;A community dedicated to helping pet owners all over the world.<br><br>Got a problem pooch or trouble with a tortoise? Get free answers from the FurryAsk.net community.</p>
  <h3 class="abs side-h" style="left:585px;top:624px">Most Active</h3>
  <div class="abs member" style="top:648px"><span class="ph"></span><span class="n">Nora Bell, DVM</span><span class="a"><span>Answers</span><span>50</span></span></div>
  <div class="abs member" style="top:716px"><span class="ph"></span><span class="n">Nora Bell, DVM</span><span class="a"><span>Answers</span><span>37</span></span></div>
  <div class="abs member" style="top:785px"><span class="ph"></span><span class="n">Nora Bell, DVM</span><span class="a"><span>Answers</span><span>33</span></span></div>
  <h3 class="abs side-h" style="left:585px;top:877px">Popular Tags</h3>
  <div class="abs tag" style="top:899px;width:147px"><span>health concerns</span><span>234</span></div>
  <div class="abs tag" style="top:919px;width:117px"><span>weight</span><span>235</span></div>
  <div class="abs tag" style="top:940px;width:96px"><span>temprament</span><span>236</span></div>
  <div class="abs tag" style="top:961px;width:80px"><span>colors</span><span>237</span></div>
  <div class="abs tag" style="top:981px;width:61px"><span>size</span><span>238</span></div>
</aside>

<footer class="abs footer">Terms | Disclaimer | Privacy | Contact | Report</footer>
</body>
</html>
```